Brenwick Homes Realty is seeking to have his informational, lead capture and Internet presence website

white and blue would be prevailed colors with scenarios of Los Angeles icons: Hollywood sign, Santa Monica pier and other beaches with palm trees. It should include information For Buyers, as well as For Sellers; common terminology in the process of purchase and selling houses and basic steps in the process of purchasing and/or selling a house.
Scroll down type of website is prefer, but tabs would be acceptable. Tabs:
About Us. For Buyers. For Sellers, Contact Us.
Links to: Terminology; process of purchase; process of selling.
Updates

Target Market(s)

Mainly focus on BUYERS.

Industry/Entity Type

California Real Estate

Coding

Coded - Design and coding required

Number of Pages Required

3 page

Colors
0054AA
0677BA
7BADD7
CADEEF
E8F1F8

Requirements
Must have
• a slogan under Brenwick Homes Realty: "Southern California Specialists Since 2004". Houses pictures must be Craftman, Country, or Ranch, but no
Nice to have
• On the first page, ABOUT US should be as a map of where to find what visitor needs: For Buyers ( description and link to2nd Page) including at the end description of the process. On 1st page also services offered For Sellers (description of what we do, -3rd page- and at the bottom, process of purchasing). Pages 2 and 3 might need a link to Terminology that will describe used terms. I see my website having at the bottom of every page with my CONTACT US information as well as invitation to send visitor's info to get personalize service. ALSO need as a legal disclaimer licenses numbers and Regulator. (To be provided to winner)
Should not have
• Listings

```html
<!DOCTYPE html>
<html lang="en">
<head>
<meta charset="utf-8">
<title>Brenwick Homes Realty</title>
<link href="https://fonts.googleapis.com/css2?family=Montserrat:wght@400;500;600;700;800&family=Oswald:wght@500;700&display=swap" rel="stylesheet">
<style>
:root{
  --blue:#0054AA;
  --blue-mid:#0677BA;
  --blue-soft:#7BADD7;
  --blue-pale:#CADEEF;
  --tint:#EEF5F8;
  --tint-2:#F3F7FA;
  --ink:#141414;
  --text:#333;
  --muted:#555;
  --white:#fff;
}
*{margin:0;padding:0;box-sizing:border-box}
html,body{width:1200px;height:3997px;overflow:hidden}
body{font-family:"Montserrat",sans-serif;color:var(--text);background:var(--white);position:relative}
section,header,nav,footer{position:relative;width:1200px}
.abs{position:absolute}
.btn{position:absolute;display:flex;align-items:center;justify-content:center;gap:10px;background:var(--blue);color:var(--white);font-size:13.5px;font-weight:600;border-radius:20px;text-decoration:none;white-space:nowrap}
.btn svg{width:10px;height:10px}
.btn-white{background:var(--white);color:var(--ink)}
h2.title{font-weight:800;font-size:32px;color:var(--ink);letter-spacing:-.3px;white-space:nowrap}
.center{text-align:center;left:0;width:1200px}
p.body{font-size:12.5px;line-height:22px;color:var(--muted)}
.photo{position:absolute}

/* top bar */
.topbar{height:40px;background:#f6f6f6;font-size:13px;color:var(--ink)}
.topbar .lic{left:160px;top:12px;word-spacing:4px}
.topbar .mail{right:162px;top:10px;display:flex;align-items:center;gap:8px}

/* nav */
.nav{height:67px;background:var(--white)}
.brand{display:flex;align-items:center;gap:10px}
.brand-mark{background:var(--blue);border-radius:4px;flex:none}
.brand-name{font-weight:800;color:var(--blue);white-space:nowrap}
.nav .brand{left:161px;top:11px}
.nav .brand-mark{width:44px;height:44px}
.nav .brand-name{font-size:19px}
.nav ul{list-style:none;position:absolute;left:573px;top:26px;display:flex;gap:24px;font-size:13px;color:var(--ink)}

/* hero */
.hero{height:514px}
.hero .photo{inset:0;background:linear-gradient(90deg,#2d5f9c 0%,#4a7cb0 28%,#8fa9bf 48%,#cfc7b6 70%,#b9c7a3 100%)}
.hero .h-1{left:162px;top:132px;font-weight:800;font-size:58px;color:var(--white);letter-spacing:1px}
.hero .h-2{left:163px;top:205px;font-family:"Oswald",sans-serif;font-weight:500;font-size:33px;color:var(--white);letter-spacing:.5px}
.hero .h-3{left:162px;top:244px;font-family:"Oswald",sans-serif;font-weight:700;font-size:68px;color:var(--white);line-height:80px;letter-spacing:1px}

/* about */
.about{height:402px;background:var(--tint)}
.about h2{top:80px}
.about p{left:215px;width:770px;top:128px;text-align:center;font-size:12px;line-height:23px}

/* figures */
.figures{height:378px}
.divider-v{left:600px;top:-34px;width:1px;height:95px;background:#7a8a9a}
.divider-dot{left:598px;top:60px;width:5px;height:5px;border-radius:50%;background:var(--blue)}
.figures .eyebrow{top:99px;font-size:14px;font-weight:600;color:var(--blue)}
.figures h2{top:128px}
.stat-num{font-weight:700;font-size:40px;color:var(--ink);line-height:44px}
.stat-label{font-size:13px;font-weight:600;letter-spacing:2.4px;color:var(--ink);line-height:18px;white-space:nowrap}
.rule{width:1px;height:70px;background:#ccd3da;top:188px}

/* buyers */
.buyers{height:662px}
.buyers .panel{left:0;top:0;width:447px;height:662px;background:var(--tint)}
.buyers .photo{left:98px;top:42px;width:441px;height:522px;background:linear-gradient(180deg,#e9eef2 0%,#a57a57 45%,#5b4a3e 65%,#6ea04a 85%,#4d8a33 100%)}
.buyers h2{left:607px;top:112px}
.buyers p{left:607px;top:155px;width:410px}
.checks{left:607px;top:240px;list-style:none;font-size:12.5px;color:var(--muted)}
.checks li{display:flex;align-items:center;gap:10px;height:26px;white-space:nowrap}
.feature{position:absolute;width:202px;height:58px;background:var(--white);box-shadow:0 3px 12px rgba(0,40,90,.1);display:flex;align-items:center;gap:14px;padding-left:16px;font-size:11px;line-height:16px;color:var(--muted)}
.feature svg{width:36px;height:36px;flex:none}

/* sellers */
.sellers{height:489px}
.sellers .photo{left:447px;top:0;width:753px;height:489px;background:linear-gradient(120deg,#e6e3dc 0%,#c9bfb3 40%,#8da6c6 70%,#6d8fbb 100%)}
.seller-card{left:160px;top:68px;width:386px;height:352px;background:var(--white);box-shadow:0 6px 24px rgba(0,0,0,.08)}
.seller-card h2{position:absolute;left:28px;top:66px}
.seller-card p{position:absolute;left:30px;top:114px;width:326px}

/* how it works */
.how{height:641px}
.how h2{top:92px}
.how .sub{top:140px;font-size:17px;color:var(--ink)}
.step{position:absolute;top:220px;width:260px;text-align:center}
.step .ring{position:relative;width:150px;height:150px;margin:0 auto}
.step .ring svg.circle{position:absolute;inset:0}
.step .num{position:absolute;left:-2px;top:104px;width:38px;height:38px;border-radius:50%;background:var(--blue);color:var(--white);font-weight:600;font-size:15px;display:flex;align-items:center;justify-content:center;border:2px solid var(--white)}
.step .icon{position:absolute;left:50px;top:50px;width:50px;height:50px}
.step h3{margin-top:20px;font-weight:500;font-size:18.5px;color:var(--ink)}
.step p{margin-top:10px;font-size:12px;line-height:20px;color:var(--muted)}
.connector{position:absolute;top:272px;width:72px;height:20px}

/* closing */
.closing{height:415px;background:var(--tint-2)}
.closing .photo{left:0;top:0;width:573px;height:415px;background:linear-gradient(180deg,#b9a8c9 0%,#e2c6c6 35%,#3f4e6e 60%,#4c5568 80%,#6f8a55 100%)}
.closing h2{left:624px;top:85px;line-height:38px}
.closing p{left:629px;top:168px;width:410px}

/* footer */
.footer{height:389px}
.footer .brand{left:0;width:1200px;justify-content:center;top:98px;gap:16px}
.footer .brand-mark{width:62px;height:62px}
.footer .brand-name{font-size:32px}
.footer ul{list-style:none;position:absolute;top:205px;left:0;width:1200px;display:flex;justify-content:center;gap:30px;font-size:12.5px;font-weight:600;color:var(--ink)}
.footer .legal{top:255px;left:240px;width:720px;text-align:center;font-size:10.5px;line-height:18px;color:var(--text)}
.footer .legal b{color:var(--ink)}
.footer .line{left:160px;top:329px;width:880px;height:1px;background:#d5d9dd}
.footer .copy{left:160px;top:353px;font-size:12px;color:var(--ink)}
.footer .terms{left:620px;top:353px;font-size:12px;color:var(--ink)}
.social{position:absolute;top:346px;left:936px;display:flex;gap:9px}
.social span{width:28px;height:28px;border:1.5px solid var(--ink);border-radius:50%}
</style>
</head>
<body>

<header class="topbar">
  <div class="abs lic">LIC #123456 &nbsp;REG #256491</div>
  <div class="abs mail">
    <svg width="18" height="16" viewBox="0 0 18 16" fill="none" stroke="#0054AA" stroke-width="1.4"><rect x="1" y="3" width="16" height="11" rx="1"/><path d="M1 4l8 6 8-6"/></svg>
    info@brenwickhomes.com
  </div>
</header>

<nav class="nav">
  <div class="abs brand"><span class="brand-mark"></span><span class="brand-name">Brenwick Homes Realty</span></div>
  <ul><li>Home</li><li>About Us</li><li>For Buyers</li><li>For Sellers</li></ul>
  <a class="btn" style="left:892px;top:16px;width:147px;height:36px">Contact Us <svg viewBox="0 0 10 10" fill="none" stroke="currentColor" stroke-width="1.3"><path d="M2 8L8 2M3 2h5v5"/></svg></a>
</nav>

<section class="hero">
  <div class="photo" role="img" aria-label="Photograph of a two-storey craftsman-style family home with a white garage and palm trees under a blue sky"></div>
  <div class="abs h-1">SOUTHERN</div>
  <div class="abs h-2">CALIFORNIA SPECIALISTS</div>
  <div class="abs h-3">SINCE 2004</div>
  <a class="btn btn-white" style="left:160px;top:337px;width:147px;height:36px">Contact Us <svg viewBox="0 0 10 10" fill="none" stroke="currentColor" stroke-width="1.3"><path d="M2 8L8 2M3 2h5v5"/></svg></a>
</section>

<section class="about">
  <h2 class="abs title center">About Brenwick Homes Realty</h2>
  <p class="abs body">Lorem ipsum dolor sit amet, consectetur adipiscing elit, sed do eiusmod tempor incididunt ut labore et dolore magna aliqua. Ut enim ad minim veniam, quis nostrud exercitation ullamco laboris nisi ut aliquipLorem ipsum dolor sit amet, consectetur adipiscing elit, sed do eiusmod tempor incididunt ut labore et dolore magna aliqua. Ut enim ad minim veniam, quis sed nostrudLorem ipsum dolor sit amet, consectetur adipiscing elit, sed do eiusmod tempor incididunt ut labore et dolore magna aliqua. Ut enim ad minim veniam, quis nostrud exercitation ullamco do</p>
  <a class="btn" style="left:444px;top:273px;width:147px;height:35px">Contact Us <svg viewBox="0 0 10 10" fill="none" stroke="currentColor" stroke-width="1.3"><path d="M2 8L8 2M3 2h5v5"/></svg></a>
  <a class="btn" style="left:608px;top:273px;width:148px;height:35px">Terminology <svg viewBox="0 0 10 10" fill="none" stroke="currentColor" stroke-width="1.3"><path d="M2 8L8 2M3 2h5v5"/></svg></a>
</section>

<section class="figures">
  <div class="abs divider-v"></div>
  <div class="abs divider-dot"></div>
  <div class="abs center eyebrow">What We Had Achieved</div>
  <h2 class="abs title center">Brenwick Homes Realty In Figures</h2>

  <svg class="abs" style="left:160px;top:196px" width="76" height="76" viewBox="0 0 76 76" fill="none" stroke="#0054AA" stroke-width="2"><path d="M6 72V20L22 6l16 14v52"/><path d="M38 40l18-14 18 14v32H38"/><rect x="14" y="24" width="6" height="6"/><rect x="24" y="24" width="6" height="6"/><rect x="14" y="36" width="6" height="6"/><rect x="24" y="36" width="6" height="6"/><rect x="50" y="52" width="12" height="20"/><path d="M2 72h72"/></svg>
  <div class="abs stat-num" style="left:267px;top:200px">20</div>
  <div class="abs stat-label" style="left:264px;top:256px">CLASSIC<br>PROJECTS</div>
  <div class="abs rule" style="left:386px"></div>

  <svg class="abs" style="left:435px;top:196px" width="84" height="76" viewBox="0 0 84 76" fill="none" stroke="#0054AA" stroke-width="2"><path d="M12 4h56v64H20"/><path d="M68 4c8 0 8 12 0 12"/><rect x="30" y="14" width="30" height="30"/><path d="M36 38V28M43 38V22M50 38V30M56 38V20"/><path d="M30 52h30M30 58h22"/><circle cx="16" cy="58" r="10"/><circle cx="16" cy="58" r="4"/></svg>
  <div class="abs stat-num" style="left:531px;top:200px">100+</div>
  <div class="abs stat-label" style="left:537px;top:256px">INDIVIDUAL PLANNING<br>CONCEPTS</div>
  <div class="abs rule" style="left:779px"></div>

  <svg class="abs" style="left:827px;top:196px" width="68" height="76" viewBox="0 0 68 76" fill="none" stroke="#0054AA" stroke-width="2"><rect x="4" y="8" width="48" height="64" rx="3"/><rect x="18" y="3" width="20" height="9" rx="2"/><rect x="12" y="24" width="7" height="7"/><rect x="12" y="38" width="7" height="7"/><rect x="12" y="52" width="7" height="7"/><path d="M24 27h18M24 41h18M24 55h18"/><circle cx="54" cy="20" r="11"/><path d="M49 20l4 4 7-8"/></svg>
  <div class="abs stat-num" style="left:905px;top:200px">15–25</div>
  <div class="abs stat-label" style="left:911px;top:256px">PROJECTS PER<br>YEAR</div>
</section>

<section class="buyers">
  <div class="abs panel"></div>
  <div class="photo" role="img" aria-label="Image of a modern two-storey house with wooden cladding, large glass windows and a green lawn"></div>
  <h2 class="abs title">For Buyers</h2>
  <p class="abs body">Lorem ipsum dolor sit amet, consectetur adipiscing elit, sed do eiusmod tempor incididunt ut labore et dolore magna aliqua. Ut enim ad minim veniam, quis nostrud exercitation</p>
  <ul class="abs checks">
    <li><svg width="13" height="13" viewBox="0 0 13 13" fill="none" stroke="#0054AA" stroke-width="1.3"><circle cx="6.5" cy="6.5" r="5.7"/><path d="M4 6.7l1.8 1.8L9 5"/></svg>Lorem ipsum dolor sit amet, consectetur adipiscing elit</li>
    <li><svg width="13" height="13" viewBox="0 0 13 13" fill="none" stroke="#0054AA" stroke-width="1.3"><circle cx="6.5" cy="6.5" r="5.7"/><path d="M4 6.7l1.8 1.8L9 5"/></svg>Lorem ipsum dolor sit amet consectetur adipiscing elit Lorem</li>
    <li><svg width="13" height="13" viewBox="0 0 13 13" fill="none" stroke="#0054AA" stroke-width="1.3"><circle cx="6.5" cy="6.5" r="5.7"/><path d="M4 6.7l1.8 1.8L9 5"/></svg>Lorem ipsum dolor sit amet consectetur</li>
  </ul>
  <div class="feature" style="left:602px;top:345px">
    <svg viewBox="0 0 36 36" fill="none" stroke="#0054AA" stroke-width="1.6"><path d="M14 22l-4-4 8-12c4-3 10-4 12-2 2 2 1 8-2 12l-12 8z"/><circle cx="23" cy="13" r="3"/><path d="M10 18l-5 1 3-6 6-1M18 26l-1 5 6-3 1-6M8 28l-4 4"/></svg>
    <span>Lorem ipsum dolor<br>sit amet consectetur</span></div>
  <div class="feature" style="left:819px;top:345px">
    <svg viewBox="0 0 36 36" fill="none" stroke="#0054AA" stroke-width="1.6"><rect x="3" y="5" width="30" height="26" rx="2"/><path d="M3 11h30"/><rect x="7" y="15" width="9" height="7"/><path d="M20 16h9M20 20h9M7 26h22"/></svg>
    <span>Lorem ipsum dolor<br>sit amet consectetur</span></div>
  <div class="feature" style="left:602px;top:420px">
    <svg viewBox="0 0 36 36" fill="none" stroke="#0054AA" stroke-width="1.6"><path d="M3 18L15 7l12 11"/><path d="M6 15v15h14"/><rect x="12" y="20" width="6" height="10"/><circle cx="27" cy="27" r="7"/><path d="M24 30l6-6M24.5 24.5h.1M29.5 29.5h.1"/></svg>
    <span>Lorem ipsum dolor<br>sit amet consectetur</span></div>
  <div class="feature" style="left:819px;top:420px">
    <svg viewBox="0 0 36 36" fill="none" stroke="#0054AA" stroke-width="1.6"><circle cx="14" cy="8" r="5"/><path d="M14 13v8M10 17h8"/><path d="M3 26h8l6 3h9l6-5-3-2-6 3h-6"/><path d="M3 22v10"/></svg>
    <span>Lorem ipsum dolor<br>sit amet consectetur</span></div>
  <a class="btn" style="left:604px;top:513px;width:214px;height:36px">Process of Purchasing <svg viewBox="0 0 10 10" fill="none" stroke="currentColor" stroke-width="1.3"><path d="M2 8L8 2M3 2h5v5"/></svg></a>
</section>

<section class="sellers">
  <div class="photo" role="img" aria-label="Photograph of a smiling couple sitting on a sofa looking at a laptop together"></div>
  <div class="abs seller-card">
    <h2 class="title">For Sellers</h2>
    <p class="body">Lorem ipsum dolor sit amet, consectetur lorem ese adipiscing elit, sed do eiusmod tempor ipsum a am incididunt ut labore et dolore magna aliqua. Ut a es enim ad minim veniam, quis nostrud exercitation aw Lorem Ipsum</p>
    <a class="btn" style="left:25px;top:251px;width:215px;height:36px">Process of Selling &nbsp;&nbsp;&nbsp;&nbsp; <svg viewBox="0 0 10 10" fill="none" stroke="currentColor" stroke-width="1.3"><path d="M2 8L8 2M3 2h5v5"/></svg></a>
  </div>
</section>

<section class="how">
  <h2 class="abs title center">How It Works</h2>
  <div class="abs center sub">Process of Purchasing Or selling Your House</div>

  <div class="step" style="left:142px">
    <div class="ring">
      <svg class="circle" viewBox="0 0 150 150"><circle cx="75" cy="75" r="73" fill="none" stroke="#7BADD7" stroke-width="1.5" stroke-dasharray="5 4"/><circle cx="75" cy="75" r="56" fill="#fff" style="filter:drop-shadow(0 3px 8px rgba(0,40,90,.15))"/></svg>
      <svg class="icon" viewBox="0 0 50 50" fill="none" stroke="#0054AA" stroke-width="2"><path d="M12 4h20l10 10v32H12z"/><path d="M32 4v10h10"/><path d="M19 22h16M19 28h16"/><circle cx="16" cy="38" r="9" fill="#fff"/><path d="M12 38l3 3 6-6"/></svg>
      <div class="num">1</div>
    </div>
    <h3>Lorem Ipsum Dolor</h3>
    <p>Lorem ipsum dolor sit consectetuer<br>adipiscing elit, sed diam nonumy<br>nibh euismod tincidunt ut.</p>
  </div>
  <svg class="connector" style="left:400px" viewBox="0 0 72 20" fill="none" stroke="#888" stroke-width="2"><path d="M2 12C22 2 46 2 64 14"/><path d="M58 8l8 7-10 2"/></svg>

  <div class="step" style="left:466px">
    <div class="ring">
      <svg class="circle" viewBox="0 0 150 150"><circle cx="75" cy="75" r="73" fill="none" stroke="#7BADD7" stroke-width="1.5" stroke-dasharray="5 4"/><circle cx="75" cy="75" r="56" fill="#fff" style="filter:drop-shadow(0 3px 8px rgba(0,40,90,.15))"/></svg>
      <svg class="icon" viewBox="0 0 50 50" fill="none" stroke="#0054AA" stroke-width="2"><path d="M12 22L28 8l16 14"/><path d="M16 19v17h24V19"/><rect x="24" y="24" width="8" height="12"/><path d="M4 34h8v12H4zM12 36h8l6 4h10"/></svg>
      <div class="num">2</div>
    </div>
    <h3>Lorem Ipsum Dolor</h3>
    <p>Lorem ipsum dolor sit consectetuer<br>adipiscing elit, sed diam nonumy<br>nibh euismod tincidunt ut.</p>
  </div>
  <svg class="connector" style="left:724px" viewBox="0 0 72 20" fill="none" stroke="#888" stroke-width="2"><path d="M2 14C22 18 46 16 64 6"/><path d="M56 4l10 1-4 9"/></svg>

  <div class="step" style="left:790px">
    <div class="ring">
      <svg class="circle" viewBox="0 0 150 150"><circle cx="75" cy="75" r="73" fill="none" stroke="#7BADD7" stroke-width="1.5" stroke-dasharray="5 4"/><circle cx="75" cy="75" r="56" fill="#fff" style="filter:drop-shadow(0 3px 8px rgba(0,40,90,.15))"/></svg>
      <svg class="icon" viewBox="0 0 50 50" fill="none" stroke="#0054AA" stroke-width="2"><circle cx="14" cy="10" r="6"/><circle cx="36" cy="10" r="6"/><path d="M4 30c0-8 4-12 10-12s10 4 10 12M26 30c0-8 4-12 10-12s10 4 10 12"/><path d="M2 32h46M8 32v14M42 32v14"/></svg>
      <div class="num">3</div>
    </div>
    <h3>Lorem Ipsum Dolor</h3>
    <p>Lorem ipsum dolor sit consectetuer<br>adipiscing elit, sed diam nonumy<br>nibh euismod tincidunt ut.</p>
  </div>

  <a class="btn" style="left:526px;top:498px;width:148px;height:35px">Get Started <svg viewBox="0 0 10 10" fill="none" stroke="currentColor" stroke-width="1.3"><path d="M2 8L8 2M3 2h5v5"/></svg></a>
</section>

<section class="closing">
  <div class="photo" role="img" aria-label="Photograph of a blue country-style house with lit windows and a double garage at dusk"></div>
  <h2 class="abs title">Lorem Ipsum Sed Amet<br>Dolor Sit Amet</h2>
  <p class="abs body">Lorem ipsum dolor sit amet, consectetur lorem ese adipiscing elit, sed do eiusmod tempor ipsum a am incididunt ut labore et dolore magna aliqua. Ut a es enim ad minim veniam, quis nostrud exercitation aw Lorem Ipsum es enim ad minim veniam, quis nostrud exercitation aw Lorem Ipsum</p>
  <a class="btn" style="left:629px;top:299px;width:147px;height:36px">Contact Us <svg viewBox="0 0 10 10" fill="none" stroke="currentColor" stroke-width="1.3"><path d="M2 8L8 2M3 2h5v5"/></svg></a>
</section>

<footer class="footer">
  <div class="abs brand"><span class="brand-mark"></span><span class="brand-name">Brenwick Homes Realty</span></div>
  <ul><li>Home</li><li>About Us</li><li>For Buyers</li><li>For Sellers</li><li>Contact Us</li></ul>
  <div class="abs legal"><b>Legal Disclaimer:</b> Lorem ipsum dolor sit amet, consectetur adipiscing elit, sed do eiusmod tempor incididunt ut labore et dolore magna aliqua. Ut enim ad minim veniam, quis nostrud exercitation ullamco laboris nisi ut aliquip</div>
  <div class="abs line"></div>
  <div class="abs copy">© 2023 Brenwick Homes Realty. All Rights Reserved.</div>
  <div class="abs terms">Term of Use | Privacy Policy</div>
  <div class="social" aria-label="Social media links"><span></span><span></span><span></span></div>
</footer>

</body>
</html>
```